Brochure for 2015 workshops

Looking for a brochure for Tip Top Tin Drum ,2015 professional development workshops. We are a creative consulting company for early childhood and looking at getting the brochure designed in a fun, recyclable and quirky design.I have attached all information needed to be included into the brochure as well as our logo.

Industry/Entity Type

It Company

```html
<!DOCTYPE html>
<html lang="en">
<head>
<meta charset="utf-8">
<title>Tip Top Tin Drum – 2015 Workshops Brochure</title>
<link href="https://fonts.googleapis.com/css2?family=Arimo:wght@400;700&display=swap" rel="stylesheet">
<style>
:root{
  --backdrop:#ece8df;
  --slab:#d3d1cd;
  --paper:#f4f2ee;
  --ink:#111111;
  --rose:#d61f5b;
  --lime:#8dc63f;
  --teal:#3a9c8e;
  --sky:#3a8fd1;
  --tangerine:#ec7d2c;
  --peach:#f7d9a8;
  --blush:#ee97a3;
  --plum:#3d2a6b;
  --cow-brown:#5a3a22;
}
*{box-sizing:border-box;margin:0;padding:0}
html,body{width:1200px;height:900px;overflow:hidden}
body{background:var(--backdrop);position:relative;font-family:"Arimo",Arial,sans-serif;color:var(--ink)}
.tile{position:absolute;width:375px;height:276px;background:var(--slab)}
.spread{position:absolute;left:22px;top:53px;width:330px;height:170px;display:flex;box-shadow:0 3px 8px rgba(0,0,0,.25)}
.page{width:50%;height:100%;background:var(--paper);position:relative;overflow:hidden}
.page + .page{border-left:1px solid #dcd8d0}
.panel{position:absolute;inset:0;width:100%;height:100%}
.title{position:absolute;left:14px;top:26px;transform:rotate(-5deg);transform-origin:left top;font-weight:700;font-size:23px;line-height:.98}
.initial{float:left;font-size:74px;line-height:.78;margin-right:2px;letter-spacing:-2px}
.copy{padding:20px 14px 0 16px;font-size:5.5px;line-height:1.45}
.copy h3{font-size:6px;margin-bottom:4px}
.copy p{margin-bottom:6px}
.details{list-style:none;font-weight:700}
/* cover tile */
.cover-spread{left:30px;top:14px;width:290px;height:148px}
.cover-spread .title{top:30px;font-size:24px}
.cover-back{position:absolute;left:56px;top:168px;width:296px;height:96px;display:flex;background:#fff;border:3px solid var(--plum);box-shadow:0 3px 8px rgba(0,0,0,.25)}
.cover-back .page{background:#fff;padding:8px}
.cover-art{width:100%;height:58px;background:linear-gradient(180deg,var(--cow-brown) 0 60%,#6aa84f 60% 80%,#2e6fb5 80%)}
.cover-name{position:absolute;left:8px;bottom:6px;font-size:13px;font-weight:700;color:var(--plum)}
</style>
</head>
<body>

<section class="tile" style="left:24px;top:20px">
  <div class="spread cover-spread">
    <div class="page">
      <svg class="panel" viewBox="0 0 145 148" preserveAspectRatio="none"><polygon points="0,0 145,0 145,118 150,130 132,120 0,128" fill="var(--rose)"/></svg>
      <div class="title"><span class="initial">Y</span>ou<br>and I</div>
    </div>
    <div class="page copy">
      <h3>You and I</h3>
      <p>Our 2015 workshops for early childhood educators. Each session is hands on, practical and fun.</p>
      <ul class="details"><li>Presenter: Jo Marsh</li><li>Date: Wednesday 18th March</li><li>Time: 9.30am to 12.30pm</li><li>Price: $65 per person</li><li>Venue: St Brigid's Hall, Elmsford</li><li>Email: bookings@tiptoptindrum.com.au</li></ul>
    </div>
  </div>
  <div class="cover-back">
    <div class="page"><div class="cover-art" role="img" aria-label="Simple geometric brown cow illustration"></div></div>
    <div class="page"><div class="cover-art" role="img" aria-label="Simple geometric brown cow illustration, facing forward"></div><span class="cover-name">tip top tin drum</span></div>
  </div>
</section>

<section class="tile" style="left:413px;top:20px">
  <div class="spread">
    <div class="page copy">
      <h3>Play Nicely</h3>
      <p>Some days working with different people is easy and some days it is hard. Explore tools that help teams play well together.</p>
      <ul class="details"><li>Presenter: Jo Marsh</li><li>Date: Wednesday 25th March</li><li>Time: 9.30am to 12.30pm</li><li>Price: $65 per person</li><li>Venue: St Brigid's Hall, Elmsford</li><li>Email: bookings@tiptoptindrum.com.au</li></ul>
    </div>
    <div class="page">
      <svg class="panel" viewBox="0 0 165 170" preserveAspectRatio="none"><polygon points="14,16 165,2 165,138 24,146 4,158 14,134" fill="var(--lime)"/></svg>
      <div class="title"><span class="initial">P</span>laying<br>Nicely..</div>
    </div>
  </div>
</section>

<section class="tile" style="left:802px;top:20px">
  <div class="spread">
    <div class="page">
      <svg class="panel" viewBox="0 0 165 170" preserveAspectRatio="none"><polygon points="0,14 150,4 150,134 162,146 146,140 0,144" fill="var(--teal)"/></svg>
      <div class="title"><span class="initial">L</span>ooking<br>in the<br>mirror</div>
    </div>
    <div class="page copy">
      <h3>Looking in the mirror</h3>
      <p>There is a lot of talk about reflective practice. This session shows simple ways to look at your own work and grow.</p>
      <ul class="details"><li>Presenter: Jo Marsh</li><li>Date: Wednesday 1st April</li><li>Time: 9.30am to 12.30pm</li><li>Price: $65 per person</li><li>Venue: St Brigid's Hall, Elmsford</li><li>Email: bookings@tiptoptindrum.com.au</li></ul>
    </div>
  </div>
</section>

<section class="tile" style="left:413px;top:312px">
  <div class="spread">
    <div class="page copy">
      <h3>Critique Mystique</h3>
      <p>Giving and receiving feedback can feel daunting. Learn friendly methods to share honest critique with colleagues and families.</p>
      <ul class="details"><li>Presenter: Lia Perkins</li><li>Date: Wednesday 8th April</li><li>Time: 9.30am to 12.30pm</li><li>Price: $65 per person</li><li>Venue: St Brigid's Hall, Elmsford</li><li>Email: bookings@tiptoptindrum.com.au</li></ul>
    </div>
    <div class="page">
      <svg class="panel" viewBox="0 0 165 170" preserveAspectRatio="none"><polygon points="12,14 165,4 165,136 22,144 2,156 12,132" fill="var(--sky)"/></svg>
      <div class="title"><span class="initial">C</span>ritique<br>Mystique</div>
    </div>
  </div>
</section>

<section class="tile" style="left:802px;top:312px">
  <div class="spread">
    <div class="page">
      <svg class="panel" viewBox="0 0 165 170" preserveAspectRatio="none"><polygon points="0,20 165,4 165,128 40,138 22,150 26,136 0,138" fill="var(--tangerine)"/></svg>
      <div class="title" style="top:40px"><span class="initial">R</span>ecycle</div>
    </div>
    <div class="page copy">
      <h3>Recycle, Reuse, Reimagine</h3>
      <p>In the hands of a child, a piece of cardboard becomes anything. Discover open ended play with found materials.</p>
      <ul class="details"><li>Presenter: Jo Marsh</li><li>Date: Tuesday 14th April</li><li>Time: 9.30am to 12.30pm</li><li>Price: $65 per person</li><li>Venue: St Brigid's Hall, Elmsford</li><li>Email: bookings@tiptoptindrum.com.au</li></ul>
    </div>
  </div>
</section>

<section class="tile" style="left:24px;top:604px">
  <div class="spread">
    <div class="page copy">
      <h3>Don't Stress the Mess</h3>
      <p>Messy play delights the senses. Find practical ways to plan, manage and enjoy messy experiences without the worry.</p>
      <ul class="details"><li>Presenter: Mia Lyons</li><li>Date: Tuesday 17th February</li><li>Time: 9.30am to 12.30pm</li><li>Price: $65 per person</li><li>Venue: St Brigid's Hall, Elmsford</li><li>Email: bookings@tiptoptindrum.com.au</li></ul>
    </div>
    <div class="page">
      <svg class="panel" viewBox="0 0 165 170" preserveAspectRatio="none"><polygon points="12,20 165,8 165,170 22,170 22,150 2,158 12,136" fill="var(--peach)"/></svg>
      <div class="title" style="top:34px"><span class="initial">D</span>on't<br>Stress<br>the Mess</div>
    </div>
  </div>
</section>

<section class="tile" style="left:413px;top:604px">
  <div class="spread">
    <div class="page">
      <svg class="panel" viewBox="0 0 165 170" preserveAspectRatio="none"><polygon points="0,22 150,12 150,122 162,134 146,130 0,150" fill="var(--blush)"/></svg>
      <div class="title" style="top:40px"><span class="initial">O</span>ut to Play</div>
    </div>
    <div class="page copy">
      <h3>Out to Play</h3>
      <p>Great ideas for outdoor spaces that invite children to explore, climb, dig and wonder in every season.</p>
      <ul class="details"><li>Presenter: Jo Marsh</li><li>Date: Tuesday 12th May</li><li>Time: 9.30am to 12.30pm</li><li>Price: $65 per person</li><li>Venue: St Brigid's Hall, Elmsford</li><li>Email: bookings@tiptoptindrum.com.au</li></ul>
    </div>
  </div>
</section>

<section class="tile" style="left:802px;top:604px">
  <div class="spread">
    <div class="page copy">
      <h3>Mr Sandman</h3>
      <p>Rest time can be a gentle part of the day. Explore calm routines that help little ones settle and sleep.</p>
      <ul class="details"><li>Presenter: Jo Marsh</li><li>Date: Tuesday 19th May</li><li>Time: 9.30am to 12.30pm</li><li>Price: $65 per person</li><li>Venue: St Brigid's Hall, Elmsford</li><li>Email: bookings@tiptoptindrum.com.au</li></ul>
    </div>
    <div class="page">
      <svg class="panel" viewBox="0 0 165 170" preserveAspectRatio="none"><polygon points="12,30 165,18 165,170 20,170 20,156 2,160 12,140" fill="var(--plum)"/></svg>
      <div class="title" style="top:44px"><span class="initial">M</span><sup style="font-size:14px">r</sup><br>Sandman</div>
    </div>
  </div>
</section>

</body>
</html>
```